Electrical Contracting business website design

Website needed to help promote an online footprint focused on local customers in my area Gympie, QLD,Australia 4570

I am after a clear website (one where my customer does not get lost or frustrated)
most important is to engage customer to Call now or Request a quote with all the lead details.

Some bread and butter work for us is broken hot water units, electrical faults and renovators

We offer all sorts of services
- smoke alarms
- Test n Tag
- Lighting
- Fans
- A/C
- Design and planning
- safety switches
- underground Power
- Energy efficient solutions
- hot water repair
- Fault finding
- Control / Automation

Target Market(s)

Local Customers, Renovators, Builders, Commercial, Industrial, Domestic

Industry/Entity Type

Electrician

Coding

Coded - Design and coding required

Number of Pages Required

1 page

Colors
f78f20
000000
ec1f27
ffffff

Requirements
Must have
• Easy to use website with clear Contact Information (call now button)
• Ph: 0491527308 24/7
• Email Brightvoltservices@examplemail.com
• , Quote request to receive leads and customer info

```html
<!DOCTYPE html>
<html lang="en">
<head>
<meta charset="utf-8">
<title>Brightvolt Electrical</title>
<link rel="stylesheet" href="https://fonts.googleapis.com/css2?family=Raleway:ital,wght@0,400;0,500;0,600;0,700;0,800;1,400;1,500;1,800&display=swap">
<style>
:root{
  --red:#ec1f27;
  --orange:#f78f20;
  --black:#000;
  --white:#fff;
  --ink:#222;
  --dark:#232323;
  --muted:#777;
  --line:#dcdcdc;
}
*{box-sizing:border-box;margin:0;padding:0}
html,body{width:1200px;height:3744px;overflow:hidden}
body{font-family:'Raleway',sans-serif;color:var(--ink);background:var(--white);position:relative}
.sec{position:absolute;left:0;width:1200px}
.abs{position:absolute}
.title{position:absolute;left:0;width:1200px;text-align:center;font-size:27px;font-weight:600;color:var(--ink)}
.title.upper{text-transform:uppercase;font-weight:600}
.divider{position:absolute;width:100px;height:16px}
.divider.center{left:550px}
.btn{position:absolute;display:flex;align-items:center;justify-content:center;font-size:10px;font-weight:700;text-transform:uppercase;letter-spacing:.2px}

/* top bar */
.topbar{top:0;height:39px;background:var(--red);color:var(--white);font-size:10px}
.topbar .contact{position:absolute;right:161px;top:13px;display:flex;gap:10px}
.topbar .sep{width:1px;height:14px;background:var(--white);margin-top:-1px}

/* nav */
.nav{top:39px;height:83px;background:var(--white)}
.brand{position:absolute;left:161px;top:30px;display:flex;align-items:center;gap:8px;font-size:16px;font-weight:700;color:var(--red)}
.brand .mark{width:14px;height:14px;background:var(--orange)}
.menu{position:absolute;right:161px;top:34px;display:flex;gap:30px;font-size:12px;font-weight:500;text-transform:uppercase;color:#333}
.menu .active{color:var(--red);text-decoration:underline}

/* hero */
.hero{top:122px;height:524px;background:linear-gradient(180deg,#3b3f3a 0%,#2f3530 45%,#3a4534 75%,#2b3127 100%)}
.hero h1{position:absolute;left:0;width:1200px;top:142px;text-align:center;font-size:45px;font-weight:800;line-height:44px;color:var(--white);text-transform:uppercase}
.hero h1 em{color:var(--red);font-style:italic}
.hero p{position:absolute;left:230px;width:740px;top:254px;text-align:center;font-size:13.5px;line-height:22px;color:var(--white)}
.hero .arrow{position:absolute;top:199px;width:45px;height:45px;border-radius:50%;display:flex;align-items:center;justify-content:center}
.hero .dots{position:absolute;top:475px;left:538px;display:flex;gap:12px}
.hero .dots span{width:33px;height:3px;background:#aaa}
.hero .dots .on{background:var(--red)}

/* about */
.about{top:646px;height:483px}
.about .lead{left:161px;top:146px;width:425px;font-size:13px;font-weight:500;line-height:21px;color:#111}
.about .body{left:161px;top:205px;width:425px;font-size:9.5px;line-height:22px;color:#666}
.about ul{position:absolute;left:161px;top:306px;list-style:none}
.about li{display:flex;align-items:center;gap:12px;font-size:11px;color:#444;height:27px}
.video{left:610px;top:149px;width:428px;height:258px;background:linear-gradient(180deg,#0d0f12 0%,#3a3530 55%,#2a2622 100%)}

/* stats */
.stats{top:1129px;height:168px;background:linear-gradient(90deg,#2b2b2b 0%,#454545 50%,#2e2e2e 100%)}
.stat{position:absolute;top:40px;width:240px;text-align:center;color:var(--white)}
.stat .num{font-size:30px;font-weight:700}
.stat .lbl{margin-top:34px;font-size:15px;text-transform:uppercase}
.stat .divider{left:70px;top:44px}

/* services */
.services{top:1297px;height:762px}
.card{position:absolute;width:280px;height:234px;border:2px solid #e2e2e2;text-align:center}
.card .icon{position:absolute;left:108px;top:-32px;width:62px;height:62px;border-radius:50%;background:var(--white);border:2px solid #ddd;display:flex;align-items:center;justify-content:center}
.card h3{position:absolute;left:0;width:100%;top:55px;font-size:13px;font-weight:600;color:#111}
.card p{position:absolute;left:30px;width:216px;top:85px;font-size:9.5px;line-height:22.5px;color:#777}
.card .btn{left:100px;top:170px;width:90px;height:28px;border:1.5px solid #ddd;color:#aaa;font-weight:600}
.card .btn.on{background:var(--red);border-color:var(--red);color:var(--white)}

/* work */
.work{top:2059px;height:611px;background:var(--dark)}
.work .title{color:var(--white)}
.work p.intro{position:absolute;left:300px;width:600px;top:140px;text-align:center;font-size:11.5px;line-height:22px;color:var(--white)}
.shot{top:222px;width:202px;height:247px}
.shot-plus{position:absolute;left:78px;top:102px;width:46px;height:44px;background:#ddd;display:flex;align-items:center;justify-content:center}

/* why / appointment */
.choose{top:2670px;height:422px}
.acc{position:absolute;left:161px;top:167px;width:429px;border:1px solid #e4e4e4}
.acc .item{height:45px;border-top:1px solid #e4e4e4;display:flex;align-items:center;justify-content:space-between;padding:0 16px;font-size:12.5px;font-style:italic;color:#999}
.acc .item:first-child{border-top:none;color:var(--red)}
.acc .open{padding:12px 16px 14px;border-top:1px solid #e4e4e4;font-size:9.5px;font-style:italic;line-height:18px;color:#666}
.field{position:absolute;height:30px;border:1px solid #e6e6e6;font-size:9.5px;font-style:italic;color:#bbb;padding:9px 11px}

/* emergency */
.emergency{top:3092px;height:200px}
.band{left:161px;top:77px;width:878px;height:112px;background:var(--red)}
.worker{left:161px;top:0;width:185px;height:189px;background:linear-gradient(180deg,#e98a2a 0%,#c98d6a 40%,#a33a2e 75%,#6b2a24 100%);border-radius:90px 90px 0 0}
.band .big{position:absolute;left:199px;top:38px;color:var(--white);font-size:25px;font-style:italic;font-weight:500;display:flex;gap:26px;align-items:baseline}
.band .big b{font-weight:800;font-style:normal}
.band .small{position:absolute;left:203px;top:76px;color:var(--white);font-size:9px;font-style:italic}
.band .btn{left:708px;top:43px;width:124px;height:29px;background:var(--white);color:var(--red)}

/* touch */
.touch{top:3292px;height:452px}
.touch h4{position:absolute;left:161px;top:160px;font-size:17px;font-weight:500;color:#111}
.touch .info{position:absolute;left:161px;top:192px;width:280px;font-size:10px;line-height:22px;color:#666}
.touch .rule{position:absolute;left:161px;top:282px;width:280px;height:1px;background:#e6e6e6}
.touch ul{position:absolute;left:161px;top:305px;list-style:none}
.touch li{display:flex;align-items:center;gap:12px;height:26px;font-size:9.5px;color:#222}
.touch .field{height:42px;padding:15px 12px;font-size:10px}
</style>
</head>
<body>

<header class="sec topbar">
  <div class="contact"><span>PHONE NUMBER: 0491527308 - 24/7</span><span class="sep"></span><span>EMAIL ADDRESS: Brightvoltservices@examplemail.com</span></div>
</header>

<nav class="sec nav">
  <div class="brand"><span class="mark"></span>Brightvolt Electrical</div>
  <div class="menu"><span class="active">Home</span><span>About</span><span>Services</span><span>Projects</span><span>Team</span><span>Contact Us</span></div>
</nav>

<section class="sec hero" role="img" aria-label="Electrician's work truck and trailer at dusk, darkened">
  <div class="arrow" style="left:161px;background:var(--white)"><svg width="12" height="12" viewBox="0 0 12 12"><path d="M8 2 4 6l4 4" stroke="#ec1f27" stroke-width="2" fill="none"/></svg></div>
  <div class="arrow" style="right:161px;background:var(--red)"><svg width="12" height="12" viewBox="0 0 12 12"><path d="M4 2l4 4-4 4" stroke="#fff" stroke-width="2" fill="none"/></svg></div>
  <h1>We provide <em>the best</em><br><em>services</em> for you</h1>
  <p>Taxidermy vegan normcore, cloud bread yuccie coloring book YOLO. Ugh lo-fi microdosing, fanny pack crucifix semiotics hella yuccie tilde bespoke 8-bit taxidermy paleo chia</p>
  <div class="btn" style="left:449px;top:344px;width:124px;height:29px;background:var(--red);color:var(--white)">Contact Now</div>
  <div class="btn" style="left:590px;top:344px;width:140px;height:29px;background:var(--white);color:var(--red)">Request a Quote</div>
  <div class="dots"><span></span><span class="on"></span><span></span></div>
</section>

<section class="sec about">
  <h2 class="title" style="top:40px">About Brightvolt Electrical</h2>
  <svg class="divider center" style="top:88px" viewBox="0 0 100 16"><path d="M0 8h38M62 8h38" stroke="#ec1f27" stroke-width="2"/><path d="M52 0 44 9h5l-2 7 8-9h-5z" fill="#ec1f27"/></svg>
  <p class="abs lead">Lorem ipsum dolor amet organic authentic normcore, subway tile plaid kitsch neutra fingerstache meggings godard pitchfork synth</p>
  <p class="abs body">IPhone migas literally, pickled direct trade bespoke hot chicken next level. Subway tileaf bicycle rights jean shorts, ugh banh mi vice occupy. Coloring book chartreuse green juice cold-pressed chia</p>
  <ul>
    <li><svg width="15" height="15" viewBox="0 0 16 16"><circle cx="8" cy="8" r="8" fill="#ec1f27"/><path d="M4.5 8.2 7 10.6l4.5-5" stroke="#fff" stroke-width="1.8" fill="none"/></svg>Valar Motem Postefiliat Idelar Ontem</li>
    <li><svg width="15" height="15" viewBox="0 0 16 16"><circle cx="8" cy="8" r="8" fill="#ec1f27"/><path d="M4.5 8.2 7 10.6l4.5-5" stroke="#fff" stroke-width="1.8" fill="none"/></svg>Valar Motem Postefiliat Idelar Ontem</li>
    <li><svg width="15" height="15" viewBox="0 0 16 16"><circle cx="8" cy="8" r="8" fill="#ec1f27"/><path d="M4.5 8.2 7 10.6l4.5-5" stroke="#fff" stroke-width="1.8" fill="none"/></svg>Valar Motem Postefiliat Idelar Ontem</li>
    <li><svg width="15" height="15" viewBox="0 0 16 16"><circle cx="8" cy="8" r="8" fill="#ec1f27"/><path d="M4.5 8.2 7 10.6l4.5-5" stroke="#fff" stroke-width="1.8" fill="none"/></svg>Valar Motem Postefiliat Idelar Ontem</li>
  </ul>
  <div class="abs video" role="img" aria-label="Video still: lit garage workshop with a red car at night">
    <svg class="abs" style="left:180px;top:95px" width="66" height="66" viewBox="0 0 66 66"><circle cx="33" cy="33" r="31" fill="#fff"/><circle cx="33" cy="33" r="25" fill="#ec1f27"/><path d="M28 22v22l17-11z" fill="#fff"/></svg>
  </div>
</section>

<section class="sec stats" role="img" aria-label="Electrician's tools on a workbench, darkened">
  <div class="stat" style="left:127px"><div class="num">715</div><svg class="divider" viewBox="0 0 100 16"><path d="M0 8h38M62 8h38" stroke="#ec1f27" stroke-width="2"/><path d="M52 0 44 9h5l-2 7 8-9h-5z" fill="#ec1f27"/></svg><div class="lbl">Install and upgrade</div></div>
  <div class="stat" style="left:367px"><div class="num">418</div><svg class="divider" viewBox="0 0 100 16"><path d="M0 8h38M62 8h38" stroke="#ec1f27" stroke-width="2"/><path d="M52 0 44 9h5l-2 7 8-9h-5z" fill="#ec1f27"/></svg><div class="lbl">Install and upgrade</div></div>
  <div class="stat" style="left:608px"><div class="num">200</div><svg class="divider" viewBox="0 0 100 16"><path d="M0 8h38M62 8h38" stroke="#ec1f27" stroke-width="2"/><path d="M52 0 44 9h5l-2 7 8-9h-5z" fill="#ec1f27"/></svg><div class="lbl">Happy clients</div></div>
  <div class="stat" style="left:848px"><div class="num">350</div><svg class="divider" viewBox="0 0 100 16"><path d="M0 8h38M62 8h38" stroke="#ec1f27" stroke-width="2"/><path d="M52 0 44 9h5l-2 7 8-9h-5z" fill="#ec1f27"/></svg><div class="lbl">Problems solved</div></div>
</section>

<section class="sec services">
  <h2 class="title upper" style="top:52px">Our Featured Services</h2>
  <svg class="divider center" style="top:100px" viewBox="0 0 100 16"><path d="M0 8h38M62 8h38" stroke="#ec1f27" stroke-width="2"/><path d="M52 0 44 9h5l-2 7 8-9h-5z" fill="#ec1f27"/></svg>

  <div class="card" style="left:161px;top:185px"><div class="icon"><svg width="34" height="34" viewBox="0 0 34 34"><circle cx="17" cy="17" r="15" fill="none" stroke="#aaa" stroke-width="2"/><circle cx="17" cy="17" r="10" fill="none" stroke="#aaa" stroke-width="2"/><path d="M17 10c3 4 5 6 5 9a5 5 0 0 1-10 0c0-2 1-3 2-4 0 2 1 3 2 3 0-3 0-5 1-8z" fill="#aaa"/></svg></div><h3>Smoke Alarms</h3><p>Lorem ipsum dolor amet organic authentic normcore, subway tile plaid kitsch neutra fingerstache meggings godard pitchfork sifa</p><div class="btn">Read More</div></div>
  <div class="card" style="left:460px;top:185px"><div class="icon" style="border-color:var(--red)"><svg width="34" height="34" viewBox="0 0 34 34"><circle cx="17" cy="17" r="15" fill="none" stroke="#ec1f27" stroke-width="2"/><circle cx="17" cy="17" r="10" fill="none" stroke="#ec1f27" stroke-width="2"/><path d="M17 10c3 4 5 6 5 9a5 5 0 0 1-10 0c0-2 1-3 2-4 0 2 1 3 2 3 0-3 0-5 1-8z" fill="#ec1f27"/></svg></div><h3>Smoke Alarms</h3><p>Lorem ipsum dolor amet organic authentic normcore, subway tile plaid kitsch neutra fingerstache meggings godard pitchfork sifa</p><div class="btn on">Read More</div></div>
  <div class="card" style="left:760px;top:185px"><div class="icon"><svg width="34" height="34" viewBox="0 0 34 34"><circle cx="17" cy="17" r="15" fill="none" stroke="#aaa" stroke-width="2"/><circle cx="17" cy="17" r="10" fill="none" stroke="#aaa" stroke-width="2"/><path d="M17 10c3 4 5 6 5 9a5 5 0 0 1-10 0c0-2 1-3 2-4 0 2 1 3 2 3 0-3 0-5 1-8z" fill="#aaa"/></svg></div><h3>Smoke Alarms</h3><p>Lorem ipsum dolor amet organic authentic normcore, subway tile plaid kitsch neutra fingerstache meggings godard pitchfork sifa</p><div class="btn">Read More</div></div>

  <div class="card" style="left:161px;top:470px"><div class="icon"><svg width="34" height="34" viewBox="0 0 34 34"><circle cx="17" cy="17" r="15" fill="none" stroke="#aaa" stroke-width="2"/><circle cx="17" cy="17" r="10" fill="none" stroke="#aaa" stroke-width="2"/><path d="M17 10c3 4 5 6 5 9a5 5 0 0 1-10 0c0-2 1-3 2-4 0 2 1 3 2 3 0-3 0-5 1-8z" fill="#aaa"/></svg></div><h3>Smoke Alarms</h3><p>Lorem ipsum dolor amet organic authentic normcore, subway tile plaid kitsch neutra fingerstache meggings godard pitchfork sifa</p><div class="btn">Read More</div></div>
  <div class="card" style="left:460px;top:470px"><div class="icon"><svg width="34" height="34" viewBox="0 0 34 34"><circle cx="17" cy="17" r="15" fill="none" stroke="#aaa" stroke-width="2"/><circle cx="17" cy="17" r="10" fill="none" stroke="#aaa" stroke-width="2"/><path d="M17 10c3 4 5 6 5 9a5 5 0 0 1-10 0c0-2 1-3 2-4 0 2 1 3 2 3 0-3 0-5 1-8z" fill="#aaa"/></svg></div><h3>Smoke Alarms</h3><p>Lorem ipsum dolor amet organic authentic normcore, subway tile plaid kitsch neutra fingerstache meggings godard pitchfork sifa</p><div class="btn">Read More</div></div>
  <div class="card" style="left:760px;top:470px"><div class="icon"><svg width="34" height="34" viewBox="0 0 34 34"><circle cx="17" cy="17" r="15" fill="none" stroke="#aaa" stroke-width="2"/><circle cx="17" cy="17" r="10" fill="none" stroke="#aaa" stroke-width="2"/><path d="M17 10c3 4 5 6 5 9a5 5 0 0 1-10 0c0-2 1-3 2-4 0 2 1 3 2 3 0-3 0-5 1-8z" fill="#aaa"/></svg></div><h3>Smoke Alarms</h3><p>Lorem ipsum dolor amet organic authentic normcore, subway tile plaid kitsch neutra fingerstache meggings godard pitchfork sifa</p><div class="btn">Read More</div></div>
</section>

<section class="sec work">
  <h2 class="title upper" style="top:52px">Our Latest Work Done</h2>
  <svg class="divider center" style="top:100px" viewBox="0 0 100 16"><path d="M0 8h38M62 8h38" stroke="#ec1f27" stroke-width="2"/><path d="M52 0 44 9h5l-2 7 8-9h-5z" fill="#ec1f27"/></svg>
  <p class="intro">Primo slide feeble ollie north nose manual helipop disaster powerslide. Cab flip full-cab method air durometer downhill masonite. Tail slob air poseur death box bearings wall ride</p>
  <div class="abs shot" style="left:161px;background:linear-gradient(135deg,#e8e8e6 0%,#c9cfc0 45%,#7a8a5a 70%,#d6d6d2 100%)" role="img" aria-label="Electrician testing a switchboard with coloured wiring"></div>
  <div class="abs shot" style="left:386px;background:linear-gradient(160deg,#1f2a3a 0%,#2d3b55 50%,#3a2b1e 100%)" role="img" aria-label="Network cabinet with patch cables">
    <div class="shot-plus"><svg width="14" height="14" viewBox="0 0 14 14"><path d="M7 1v12M1 7h12" stroke="#ec1f27" stroke-width="2"/></svg></div>
  </div>
  <div class="abs shot" style="left:610px;background:linear-gradient(135deg,#2a2c2e 0%,#575b60 50%,#1e1f21 100%)" role="img" aria-label="Rack of server units"></div>
  <div class="abs shot" style="left:835px;background:linear-gradient(180deg,#7ea2c8 0%,#b9cde0 55%,#6f7a62 85%,#4e5a42 100%)" role="img" aria-label="High-voltage transmission tower against the sky"></div>
  <svg class="abs" style="left:551px;top:499px" width="48" height="37" viewBox="0 0 48 37"><path d="M12 0h36L36 37H0z" fill="#ec1f27"/><path d="M27 13l-5 5.5 5 5.5" stroke="#fff" stroke-width="2" fill="none"/></svg>
  <svg class="abs" style="left:603px;top:499px" width="48" height="37" viewBox="0 0 48 37"><path d="M12 0h36L36 37H0z" fill="#555"/><path d="M22 13l5 5.5-5 5.5" stroke="#777" stroke-width="2" fill="none"/></svg>
</section>

<section class="sec choose">
  <h2 class="abs" style="left:161px;width:429px;top:52px;text-align:center;font-size:27px;font-weight:600;text-transform:uppercase">Why Choose Us</h2>
  <svg class="divider" style="left:325px;top:102px" viewBox="0 0 100 16"><path d="M0 8h38M62 8h38" stroke="#ec1f27" stroke-width="2"/><path d="M52 0 44 9h5l-2 7 8-9h-5z" fill="#ec1f27"/></svg>
  <h2 class="abs" style="left:610px;width:429px;top:52px;text-align:center;font-size:27px;font-weight:600;text-transform:uppercase">Make an Appointment</h2>
  <svg class="divider" style="left:774px;top:102px" viewBox="0 0 100 16"><path d="M0 8h38M62 8h38" stroke="#ec1f27" stroke-width="2"/><path d="M52 0 44 9h5l-2 7 8-9h-5z" fill="#ec1f27"/></svg>

  <div class="acc">
    <div class="item">15Years Experienced<svg width="12" height="12" viewBox="0 0 12 12"><path d="M1 6h10" stroke="#ec1f27" stroke-width="2"/></svg></div>
    <div class="open">Effective communication is the key to success for any business. From our staff, to our field technicians, it is vital to us to always keep our clients</div>
    <div class="item">Affordable Prices<svg width="12" height="12" viewBox="0 0 12 12"><path d="M6 1v10M1 6h10" stroke="#ccc" stroke-width="1.5"/></svg></div>
    <div class="item">Service Provider 24/7<svg width="12" height="12" viewBox="0 0 12 12"><path d="M6 1v10M1 6h10" stroke="#ccc" stroke-width="1.5"/></svg></div>
  </div>

  <div class="field" style="left:610px;top:168px;width:203px">First Name</div>
  <div class="field" style="left:835px;top:168px;width:204px">Last Name</div>
  <div class="field" style="left:610px;top:209px;width:203px">Address</div>
  <div class="field" style="left:835px;top:209px;width:204px">Phone Number</div>
  <div class="field" style="left:610px;top:250px;width:203px">Time</div>
  <div class="field" style="left:835px;top:250px;width:204px">Date</div>
  <div class="field" style="left:610px;top:291px;width:203px">Apt/Suit</div>
  <div class="field" style="left:835px;top:291px;width:204px">Service Description</div>
  <div class="btn" style="left:610px;top:334px;width:429px;height:29px;background:var(--red);color:var(--white)">Make Appointment Now</div>
</section>

<section class="sec emergency">
  <div class="abs band">
    <div class="big"><b>24 / 7</b><span>Emergency Call: 0491527308</span></div>
    <div class="small">Lorem Ipsum Dolor Amet Ningun Postekam Doledar Valar Dohaeris If Stored Any</div>
    <div class="btn">Contact Now</div>
  </div>
  <div class="abs worker" role="img" aria-label="Electrician in an orange hard hat and plaid shirt"></div>
</section>

<section class="sec touch">
  <h2 class="title upper" style="top:44px">Keep in Touch</h2>
  <svg class="divider center" style="top:93px" viewBox="0 0 100 16"><path d="M0 8h38M62 8h38" stroke="#ec1f27" stroke-width="2"/><path d="M52 0 44 9h5l-2 7 8-9h-5z" fill="#ec1f27"/></svg>
  <h4>Contact Information</h4>
  <p class="info">Whether you have any question about our features, service pricing or anything else our team is ready to answer all your questions</p>
  <div class="rule"></div>
  <ul>
    <li><svg width="13" height="15" viewBox="0 0 13 16"><path d="M6.5 0A6 6 0 0 0 .5 6c0 4.5 6 10 6 10s6-5.5 6-10a6 6 0 0 0-6-6z" fill="#ec1f27"/><circle cx="6.5" cy="6" r="2.3" fill="#fff"/></svg>LOCATION: Lorem ipsum street 3042, Avenue 2</li>
    <li><svg width="13" height="13" viewBox="0 0 14 14"><path d="M3 0l3 3-2 2c1 2 3 4 5 5l2-2 3 3-2 3C6 14 0 8 0 3z" fill="#ec1f27"/></svg>PHONE NUMBER: 0491527308 - 24/7</li>
    <li><svg width="13" height="11" viewBox="0 0 14 11"><rect width="14" height="11" fill="#ec1f27"/><path d="M0 0l7 6 7-6" stroke="#fff" stroke-width="1.3" fill="none"/></svg>EMAIL ADDRESS: Brightvoltservices@examplemail.com</li>
  </ul>
  <div class="field" style="left:462px;top:160px;width:277px">First Name</div>
  <div class="field" style="left:761px;top:160px;width:278px">Last Name</div>
  <div class="field" style="left:462px;top:216px;width:277px">Phone Number</div>
  <div class="field" style="left:761px;top:216px;width:278px">E-mail Address</div>
  <div class="field" style="left:462px;top:273px;width:277px">Service</div>
  <div class="field" style="left:761px;top:273px;width:278px">Subject</div>
  <div class="btn" style="left:537px;top:328px;width:425px;height:41px;background:var(--red);color:var(--white)">Send Message</div>
</section>

</body>
</html>
```